Hadley & Partners, LLC Business Card 2016

We need a new business card design for a very important trade show coming up.

We are a compliance Consulting Firm. Our clients are stock brokerage firms and investment advisers.

I would like our logo on both sides of the card.

Info in the front of the card shold include:

Logo
First & Last Name
Title
Office #
Cell #
Email
Company Address (42 W. Calloway St., Suite 300 Pasadena, CA 91417

Back of the card should include the logo and url: www.hadleypartnersgroup.com

Target Market(s)

Stock Brokerage Firms and Investment Advisers

Industry/Entity Type

Financial Service

Contact Information for Business Card

Marcus J. Pellew
President
42 W. Calloway St., Suite 300
Pasadena, CA 91417
O 626.555.0147 ext. 204
C 818.555.0193
Email: marcus@hadleypartnersgroup.com
www.hadleypartnersgroup.com

Requirements
Nice to have
• The back of the card could be black with the logo with the white letters.
• I do want the front of the card to at least have the color logo with the black "Hadley & Partners Lettering.

```html
<!DOCTYPE html>
<html lang="en">
<head>
<meta charset="utf-8">
<title>Hadley &amp; Partners — Business Card</title>
<link rel="stylesheet" href="https://fonts.googleapis.com/css2?family=Cinzel:wght@400&family=Open+Sans:wght@400;600&display=swap">
<style>
  :root {
    --page-bg: #e9e6e1;
    --card-black: #1c1c1d;
    --card-black-edge: #111112;
    --card-white: #ffffff;
    --card-white-shade: #eef0f1;
    --brand-white: #ffffff;
    --brand-black: #1a1a1a;
    --brand-red: #d8262f;
    --mark-red: #e0403f;
    --text-grey: #333333;
  }
  * { margin: 0; padding: 0; box-sizing: border-box; }
  html, body {
    width: 1200px;
    height: 1023px;
    overflow: hidden;
    background: var(--page-bg);
  }
  .canvas {
    width: 1200px;
    height: 1023px;
    display: flex;
    flex-direction: column;
    align-items: center;
    justify-content: center;
    gap: 56px;
  }
  .card {
    position: relative;
    width: 700px;
    height: 400px;
    border-radius: 4px;
    box-shadow: 0 14px 32px rgba(0,0,0,0.22);
    overflow: hidden;
  }

  /* Back */
  .card-back {
    background: linear-gradient(160deg, #262627 0%, var(--card-black) 55%, var(--card-black-edge) 100%);
  }
  .brand {
    display: flex;
    align-items: center;
    gap: 22px;
  }
  .brand-square {
    flex: none;
    background: var(--mark-red);
  }
  .brand-name {
    font-family: "Cinzel", "Times New Roman", serif;
    font-weight: 400;
    line-height: 1;
  }
  .brand-name .primary { display: block; }
  .brand-name .secondary { display: block; }

  .card-back .brand {
    position: absolute;
    left: 120px;
    top: 120px;
  }
  .card-back .brand-square { width: 80px; height: 80px; }
  .card-back .brand-name { color: var(--brand-white); }
  .card-back .brand-name .primary { font-size: 60px; letter-spacing: 2px; }
  .card-back .brand-name .secondary { margin-top: 6px; font-size: 21px; letter-spacing: 13px; }
  .card-url {
    position: absolute;
    right: 100px;
    bottom: 90px;
    font-family: "Open Sans", Arial, sans-serif;
    font-size: 22px;
    letter-spacing: 2px;
    color: var(--brand-red);
  }

  /* Front */
  .card-front {
    background: var(--card-white);
  }
  .front-shade {
    position: absolute;
    right: 0;
    top: 0;
    width: 340px;
    height: 400px;
    background: linear-gradient(135deg, var(--card-white) 0%, var(--card-white-shade) 100%);
  }
  .card-front .brand {
    position: absolute;
    left: 56px;
    top: 52px;
    gap: 14px;
  }
  .card-front .brand-square { width: 44px; height: 44px; }
  .card-front .brand-name { color: var(--brand-black); }
  .card-front .brand-name .primary { font-size: 32px; letter-spacing: 1px; }
  .card-front .brand-name .secondary { margin-top: 4px; font-size: 11px; letter-spacing: 7px; }

  .person {
    position: absolute;
    left: 56px;
    top: 150px;
    font-family: "Open Sans", Arial, sans-serif;
    color: var(--brand-black);
  }
  .person-name { font-size: 22px; font-weight: 600; }
  .person-title { margin-top: 2px; font-size: 15px; color: var(--text-grey); }

  .contact {
    position: absolute;
    left: 56px;
    bottom: 46px;
    font-family: "Open Sans", Arial, sans-serif;
    font-size: 15px;
    line-height: 1.6;
    color: var(--text-grey);
    list-style: none;
  }
  .contact .label {
    display: inline-block;
    width: 18px;
    color: var(--brand-red);
  }
  .address {
    position: absolute;
    right: 56px;
    bottom: 46px;
    font-family: "Open Sans", Arial, sans-serif;
    font-style: normal;
    font-size: 15px;
    line-height: 1.6;
    text-align: right;
    color: var(--text-grey);
  }
</style>
</head>
<body>
  <main class="canvas">
    <section class="card card-back" aria-label="Business card back">
      <div class="brand">
        <div class="brand-square" aria-hidden="true"></div>
        <h1 class="brand-name">
          <span class="primary">HADLEY</span>
          <span class="secondary">&amp; PARTNERS</span>
        </h1>
      </div>
      <p class="card-url">www.hadleypartnersgroup.com</p>
    </section>

    <section class="card card-front" aria-label="Business card front">
      <div class="front-shade" role="img" aria-label="Soft light grey background shading"></div>
      <div class="brand">
        <div class="brand-square" aria-hidden="true"></div>
        <h2 class="brand-name">
          <span class="primary">HADLEY</span>
          <span class="secondary">&amp; PARTNERS</span>
        </h2>
      </div>
      <div class="person">
        <p class="person-name">Marcus J. Pellew</p>
        <p class="person-title">President</p>
      </div>
      <ul class="contact">
        <li><span class="label">C</span>818.555.0193</li>
        <li><span class="label">O</span>626.555.0147 ext. 204</li>
        <li>marcus@hadleypartnersgroup.com</li>
      </ul>
      <address class="address">
        42 W. Calloway St., Suite 300<br>
        Pasadena, CA 91417
      </address>
    </section>
  </main>
</body>
</html>
```